Buch-/E-Book-Cover für einen Eltern-Ratgeber
Zielgruppe
Ich bin Autor/Self-Publisher von Büchern/E-Books.
Aufgabenstellung
Ich benötige ein Buchcover (Print Paperback und E-Book) für einen kurzen Eltern-Ratgeber (ca. 60 Seiten):
Titel: 'Morgens glänzt das Lächeln'
Autorin: Mira Oltenbrück
MO Verlag, Berlin
Das Buch richtet sich an verzweifelte Eltern und gibt Tipps, wie sie ihre kleinen Kinder zum Zähne putzen animieren können. Für die Gestaltung gerne vorzugsweise Fotos von echten Menschen (Eltern + Kind bzw. nur Kind bzw. 2 Kinder). Illustrierte Cover sind auch OK, aber nicht präferiert. Für Vorschläge bitte *inklusive Rückseite* und an bestehenden Eltern-Ratgebern orientieren, die Lesofant zu finden sind, wie zum Beispiel:
- Wiegenzeit von Falk T. Brünning
- OMA auf Achse von Ute Brembach
- Kleine Helden wachsen mit Mut von Birte Solander
- Grenzen setzen ohne Streit von Gudrun Pell-Wiemer
Auf den Buchseiten sind Illustrationen enthalten, die mit dem Buchcover möglichst auch harmonisieren sollten. Die Entwürfe der Illustrationen sind hier hochgeladen.
Ggf. kann man mit einer Text-Banderole/Kreis arbeiten, mit der Aufschrift '21 praktische Tipps für Eltern'
Klappentext:
Ihr Kind will sich partout nicht die Zähne putzen? Jedes Bitten und Flehen sind vergebens?
Für viele Eltern von kleinen Kindern ist es ein täglicher K(r)ampf im Bad. Ein ewiges Theater und langes Diskutieren. Niemand möchte sein Kind zwingen, schon gar nicht körperlich. Aber ohne Zähneputzen keine gesunden und schönen Zähne. Was also tun?
Nicht verzweifeln! Alle geplagten Eltern von Zwei- bis Fünfjährigen finden in diesem Büchlein 21 kurze und praktische Tipps, wie sie ihr Kind zum Zähneputzen animieren können. So wird das Zähneputzen ein fester Bestandteil der Morgen- und Abendroutine. Mit Spaß und Freude und ohne Graus. Probieren Sie die Tipps heute noch aus!

```html
<!DOCTYPE html>
<html lang="de">
<head>
<meta charset="utf-8">
<title>Morgens glänzt das Lächeln – Cover</title>
<link rel="stylesheet" href="https://fonts.googleapis.com/css2?family=Roboto+Condensed:wght@400;700&family=Ubuntu:wght@400&display=swap">
<style>
  :root {
    --backdrop: #95c9b6;
    --paper: #ffffff;
    --paper-shade: #f3f3f3;
    --red: #e65140;
    --green: #21946b;
    --ink: #1d1d1d;
    --hair: #8a5a34;
    --skin: #e8b596;
    --shirt: #e0412f;
  }
  * { box-sizing: border-box; margin: 0; padding: 0; }
  html, body { width: 1200px; height: 1195px; overflow: hidden; }
  body {
    background: var(--backdrop);
    font-family: "Roboto Condensed", "Arial Narrow", sans-serif;
    color: var(--ink);
  }
  .spread {
    position: absolute;
    top: 218px;
    left: 60px;
    display: flex;
    gap: 40px;
  }
  .cover {
    position: relative;
    width: 520px;
    height: 758px;
    background: linear-gradient(180deg, var(--paper) 0%, var(--paper-shade) 100%);
    overflow: hidden;
    box-shadow: 0 10px 30px rgba(0, 0, 0, 0.18);
  }

  /* Front */
  .front-author {
    position: absolute;
    top: 40px;
    width: 100%;
    text-align: center;
    font-family: "Ubuntu", sans-serif;
    font-size: 17px;
    letter-spacing: 0.2px;
  }
  .front-title {
    position: absolute;
    top: 92px;
    width: 100%;
    text-align: center;
    font-weight: 700;
    font-size: 60px;
    line-height: 1.08;
    text-shadow: 0 6px 10px rgba(0, 0, 0, 0.12);
  }
  .front-title .accent { color: var(--red); }
  .front-title .main { color: var(--green); }
  .front-photo {
    position: absolute;
    left: 28px;
    right: 28px;
    top: 280px;
    bottom: 0;
    border-radius: 46% 46% 0 0 / 30% 30% 0 0;
    background: linear-gradient(180deg,
      var(--hair) 0%, var(--hair) 14%,
      var(--skin) 30%, var(--skin) 56%,
      var(--shirt) 64%, var(--shirt) 100%);
    opacity: 0.92;
  }
  .tip-band {
    position: absolute;
    left: 40px;
    top: 640px;
    width: 460px;
    height: 70px;
    transform: rotate(-3.5deg);
  }
  .tip-band-pill {
    position: absolute;
    left: 26px;
    right: 0;
    top: 4px;
    height: 60px;
    background: var(--green);
    border-radius: 30px;
  }
  .tip-band-count {
    position: absolute;
    left: 0;
    top: -8px;
    font-weight: 700;
    font-size: 70px;
    line-height: 1;
    color: var(--paper);
    letter-spacing: -3px;
  }
  .tip-band-label {
    position: absolute;
    left: 82px;
    top: 14px;
    font-weight: 700;
    font-size: 30px;
    line-height: 1.2;
    color: var(--paper);
  }

  /* Back */
  .back-content {
    position: absolute;
    inset: 42px 36px 0;
    text-align: center;
  }
  .back-hook {
    color: var(--red);
    font-weight: 700;
    font-size: 30px;
    line-height: 1.2;
  }
  .back-body {
    margin-top: 30px;
    font-size: 20px;
    line-height: 1.35;
  }
  .back-shout {
    margin-top: 26px;
    color: var(--green);
    font-weight: 700;
    font-size: 56px;
    line-height: 1.1;
  }
  .back-cta {
    margin-top: 32px;
    color: var(--red);
    font-weight: 700;
    font-size: 28px;
    line-height: 1.2;
  }
</style>
</head>
<body>
  <main class="spread">
    <section class="cover cover-front">
      <p class="front-author">Mira Oltenbrück</p>
      <h1 class="front-title">
        <span class="accent">Morgens glänzt</span> <span class="main">das</span><br>
        <span class="main">Lächeln</span>
      </h1>
      <div class="front-photo" role="img" aria-label="Foto: lächelndes Mädchen mit braunen Haaren und rotem T-Shirt hält eine grüne Zahnbürste"></div>
      <div class="tip-band">
        <div class="tip-band-pill"></div>
        <span class="tip-band-count">21</span>
        <span class="tip-band-label">praktische Tipps für Eltern</span>
      </div>
    </section>

    <section class="cover cover-back">
      <div class="back-content">
        <h2 class="back-hook">Ihr Kind will sich partout nicht die Zähne putzen? Jedes Bitten und Flehen ist vergebens?</h2>
        <p class="back-body">Für viele Eltern von kleinen Kindern ist es ein täglicher K(r)ampf im Bad. Ein ewiges Theater und langes Diskutieren. Niemand möchte sein Kind zwingen, schon gar nicht körperlich. Aber ohne Zähneputzen keine gesunden und schönen Zähne. Was also tun?</p>
        <p class="back-shout">Nicht verzweifeln!</p>
        <p class="back-body">Alle geplagten Eltern von Zwei- bis Fünfjährigen finden in diesem Büchlein 21 kurze und praktische Tipps, wie sie Ihr Kind zum Zähneputzen animieren können. So wird das Zähneputzen ein fester Bestandteil der Morgen- und Abendroutine. Mit Spaß und Freude und ohne Graus.</p>
        <p class="back-cta">Probieren Sie die Tipps<br>heute noch aus!</p>
      </div>
    </section>
  </main>
</body>
</html>
```